2 Business Card Designs

Need two business cards designed:
1) for lumora films (wedding video) website is lumorafilms.com.au
2) for lumora films (corporate video) website is lumorafilms.net.au

I am looking for something simple, no fancy shapes etc. Just elegant, simple and classy.

Both companies are video companies, one specialising in weddings the other corporate videos. Neither card needs to have any pics of video or camera related images. Please use same colour schemes as respective websites.

Logo is the same but can change colour.

Industry/Entity Type

Camera

Requirements
Must have
• Logo should be either all white or a colour to match websites
Should not have
• swirls, flowers, shapes, etc.

```html
<!DOCTYPE html>
<html lang="en">
<head>
<meta charset="utf-8">
<title>lumora films — business cards</title>
<link rel="stylesheet" href="https://fonts.googleapis.com/css2?family=Arimo:wght@400&display=swap">
<style>
  :root {
    --sage: #cbcdac;
    --olive: #6a6548;
    --band: #6b6a55;
    --ink: #6b6a50;
    --ink-soft: #8c8b74;
    --paper: #ffffff;
    --on-dark: #e8e6d6;
    --edge: #2f2f2f;
  }
  * { box-sizing: border-box; margin: 0; padding: 0; }
  html, body {
    width: 709px; height: 1200px; overflow: hidden;
    background: var(--paper);
    font-family: "Arimo", Arial, sans-serif;
  }
  .sheet { position: relative; width: 709px; height: 1200px; }

  .card {
    position: absolute; left: 81px; width: 546px; height: 333px;
    border: 1px solid var(--edge); border-radius: 26px; overflow: hidden;
    background: var(--paper);
  }
  .card--front { top: 69px; background: var(--sage); }
  .card--back-dark { top: 433px; }
  .card--back-light { top: 796px; }

  .wordmark { color: var(--ink); font-weight: 400; line-height: 1; }
  .wordmark__name { display: block; letter-spacing: -1px; }
  .wordmark__sub { display: block; text-transform: uppercase; }

  .card--front .wordmark { position: absolute; top: 118px; left: 0; width: 100%; text-align: center; }
  .card--front .wordmark__name { font-size: 70px; }
  .card--front .wordmark__sub { font-size: 25px; letter-spacing: 15px; margin-top: 4px; padding-left: 15px; }

  .url-band {
    position: absolute; top: 221px; left: 0; width: 100%; height: 35px;
    background: var(--band); color: #fff; font-size: 21px;
    display: flex; align-items: center; justify-content: center;
  }

  .half { position: absolute; top: 0; height: 100%; width: 50%; }
  .half--left { left: 0; }
  .half--right { right: 0; }
  .half--olive { background: var(--olive); }
  .half--sage { background: var(--sage); }

  .half .wordmark { position: absolute; top: 50px; left: 41px; width: 176px; text-align: center; }
  .half .wordmark__name { font-size: 48px; }
  .half .wordmark__sub { font-size: 16px; letter-spacing: 10px; margin-top: 1px; padding-left: 10px; }

  .person { position: absolute; top: 155px; left: 46px; color: var(--ink); }
  .person__name { font-size: 28px; line-height: 1; }
  .person__role { font-size: 18px; margin-top: 9px; color: var(--ink-soft); }

  .details { position: absolute; top: 249px; font-size: 14px; line-height: 17px; color: var(--ink-soft); }
  .half--left .details { left: 46px; }
  .half--right .details { left: 20px; }
  .half--olive .details { color: var(--on-dark); }
</style>
</head>
<body>
<main class="sheet">

  <section class="card card--front" aria-label="Card front">
    <div class="wordmark">
      <span class="wordmark__name">lumora</span>
      <span class="wordmark__sub">films</span>
    </div>
    <div class="url-band">www.lumorafilms.com.au</div>
  </section>

  <section class="card card--back-dark" aria-label="Card back, olive version">
    <div class="half half--left">
      <div class="wordmark">
        <span class="wordmark__name">lumora</span>
        <span class="wordmark__sub">films</span>
      </div>
      <div class="person">
        <p class="person__name">Daniel Hart</p>
        <p class="person__role">managing director</p>
      </div>
      <p class="details">218 Harbour Road<br>Linfield :: NSW :: 2073<br>Phone: +61 2 9410 3827</p>
    </div>
    <div class="half half--right half--olive">
      <p class="details">Monday-Friday 9am-5pm<br>Evening Viewings available<br>All bookings via appointment only</p>
    </div>
  </section>

  <section class="card card--back-light" aria-label="Card back, sage version">
    <div class="half half--left half--sage">
      <div class="wordmark">
        <span class="wordmark__name">lumora</span>
        <span class="wordmark__sub">films</span>
      </div>
      <div class="person">
        <p class="person__name">Daniel Hart</p>
        <p class="person__role">managing director</p>
      </div>
      <p class="details">218 Harbour Road<br>Linfield :: NSW :: 2073<br>Phone: +61 2 9410 3827</p>
    </div>
    <div class="half half--right">
      <p class="details">Monday-Friday 9am-5pm<br>Evening Viewings available<br>All bookings via appointment only</p>
    </div>
  </section>

</main>
</body>
</html>
```